www.HarborviewSmileGlow.com needs to be re-designed

Current website to be redesigned www.HarborviewSmileGlow.com

*Need a custom-made new theme

I need all 10 pages redesigned using existing content.
I need the website to be revamped to a more modern look.

Please start with Homepage first then after homepage mock up is approved we can move forward with rest of pages.

Please use existing images from my Facebook or Instagram page of our real customers for banner image...

(Where to find my FB and IG pages...
You can access these pages from the website header and "contact us" page for address.)

I would like to have a button that says "Book Appointment Online" and get rid of the actual form that is on current website.

But other than that please include all other content, features, etc in mock ups so I can make a decision on the website.

I prefer custom design and must be WP installable responsive theme.

This is design-only. I am open to any concepts you can submit.

Target Market(s)

people that care about thier looks

Industry/Entity Type

Dental Clinic

Colors

Designer to choose colors to be used in the design.

Requirements
Must have
• All current content/text that is currently on website. Just formatted so it doesnt look so busy. I want to make emphasis on BOOK APPOINTMENT button and $99 SPECIAL BUTTON
Nice to have
• White background so everything pops
Should not have
• I do not like stock photo images, please use images from my facebook and IG page of real customers or even a snap shot of our office building. You can access these pages from the website header and contact us page for address, maybe yu can use snapshot somewhere of building of our address on homepage possibly in banner image.

```html
<!DOCTYPE html>
<html lang="en">
<head>
<meta charset="utf-8">
<title>Harborview Smile Glow – Home</title>
<link href="https://fonts.googleapis.com/css2?family=Open+Sans:wght@400;600;700&family=Oswald:wght@500&display=swap" rel="stylesheet">
<style>
:root{
  --blue:#1ba8d6;
  --blue-dark:#1791bb;
  --slate:#44596a;
  --slate-dark:#3a4d5c;
  --ink:#3c4a55;
  --muted:#6f7c86;
  --line:#c9d1d7;
  --paper:#ffffff;
  --soft:#f1f3f5;
}
*{box-sizing:border-box;margin:0;padding:0}
html,body{width:1200px;height:3636px;overflow:hidden}
body{font-family:"Open Sans",Arial,sans-serif;color:var(--ink);background:var(--paper);font-size:14px;line-height:1.55}
.wrap{position:relative;width:890px;margin:0 auto;height:100%}
section,header,nav,footer{position:relative;width:1200px;overflow:hidden}

/* header */
.site-header{height:116px}
.brand{position:absolute;left:0;top:18px;display:flex;align-items:center;gap:12px}
.brand-dot{width:70px;height:70px;border-radius:50%;background:var(--soft);border:3px solid var(--blue)}
.brand-name{font-weight:700;font-size:27px;color:var(--slate);line-height:1.05;width:190px}
.top-contact{position:absolute;right:0;top:12px;display:flex;align-items:center;gap:18px;font-size:15px}
.top-contact .call{color:var(--blue);font-weight:600}
.socials{display:flex;gap:8px;align-items:center;color:var(--muted)}
.socials i{display:block;width:12px;height:12px;border-radius:50%;background:var(--muted)}
.socials b{font-weight:400;font-size:12px}
.top-buttons{position:absolute;right:0;top:56px;display:flex;gap:22px}
.btn{display:inline-flex;align-items:center;justify-content:center;height:40px;padding:0 26px;color:#fff;font-size:14px;font-weight:600;text-decoration:none}
.btn-book{background:var(--slate);width:207px}
.btn-deal{background:var(--blue);width:280px}

/* nav */
.main-nav{height:44px;background:var(--blue)}
.main-nav ul{list-style:none;display:flex;height:44px;align-items:stretch}
.main-nav li{display:flex;align-items:center;padding:0 17px;color:#fff;font-size:13.5px;font-weight:600}
.main-nav li.active{background:var(--slate)}

/* hero */
.hero{height:434px;background:linear-gradient(100deg,#d9dde0 0%,#eceeef 45%,#cfd6db 100%)}
.hero-photo{position:absolute;left:430px;top:0;width:770px;height:434px;background:linear-gradient(90deg,#c9cfd3,#e6e8ea 40%,#bfc8cf 75%,#d8dcdf)}
.hero-panel{position:absolute;left:0;top:0;width:560px;height:434px}
.hero-text{position:absolute;left:130px;top:88px;color:#fff}
.hero-text .kicker{font-size:21px}
.hero-text .special{font-size:25px;font-weight:700;color:var(--blue);line-height:1.1}
.hero-text .offer{font-size:19px;font-weight:700;line-height:1.35;margin-top:18px;width:280px}
.hero-text .btn{margin-top:20px;height:40px;background:var(--blue);font-size:16px;padding:0 20px;gap:8px}
.hero-dots{position:absolute;left:133px;top:352px;display:flex;gap:12px}
.circle-btn{width:34px;height:34px;border-radius:50%;display:flex;align-items:center;justify-content:center}
.circle-btn.light{background:#fff}
.circle-btn.blue{background:var(--blue)}
.circle-btn.slate{background:var(--slate)}

/* welcome */
.welcome{height:424px}
.welcome-text{position:absolute;left:155px;top:42px;width:415px}
.welcome-text h1{font-weight:400;font-size:24px;color:var(--slate);line-height:1.3}
.welcome-text h1 span{display:block;color:var(--blue);font-weight:600;font-size:20px}
.welcome-text .lead{color:var(--blue);font-weight:700;font-size:13px;margin-top:24px}
.welcome-text p{font-size:13px;color:var(--muted);line-height:1.5}
.welcome-text p + p{margin-top:18px}
.welcome-photo{position:absolute;left:600px;top:0;width:600px;height:424px;background:linear-gradient(120deg,#d8dadc,#eff0f0 45%,#c5cbd0)}

/* why */
.why{height:320px;background:var(--slate);color:#fff}
.section-title{text-align:center;font-size:19px;font-weight:700;padding-top:42px}
.section-title::after{content:"";display:block;width:40px;height:2px;background:var(--blue);margin:8px auto 0}
.why .section-title::after{background:#fff}
.why-list{position:absolute;left:155px;top:115px;width:890px;display:flex;justify-content:space-between;list-style:none}
.why-list li{width:160px;height:160px;border-radius:50%;background:var(--blue);display:flex;flex-direction:column;align-items:center;justify-content:center;gap:10px;font-size:16px;font-weight:600}
.why-list svg{width:54px;height:54px}

/* how */
.how{height:432px}
.how-photo{position:absolute;left:0;top:0;width:600px;height:432px;background:linear-gradient(110deg,#b99884,#e0cdbd 45%,#cfd3cf 70%,#9ea797)}
.how-text{position:absolute;left:662px;top:48px;width:400px}
.how-text h2{font-size:19px;font-weight:600;color:var(--slate);margin-bottom:26px}
.how-text p{font-size:13px;color:var(--muted);line-height:1.5}
.how-text p + p{margin-top:18px}

/* compare */
.compare{height:376px;background:var(--soft)}
.compare .section-title{color:var(--slate)}
.compare .section-title::after{background:var(--slate)}
.compare-table{position:absolute;left:155px;top:100px;width:795px;border-collapse:collapse;font-size:12.5px;color:var(--muted)}
.compare-table th{height:48px;color:#fff;font-size:16px;font-weight:600;background:var(--slate);border-left:2px solid var(--soft)}
.compare-table th.hl{background:var(--blue)}
.compare-table th.us{background:var(--paper);color:var(--slate);font-size:15px;font-weight:700}
.compare-table td{height:30px;text-align:center;border-bottom:1px dashed var(--line);border-left:1px dashed var(--line)}
.compare-table td:first-child{border-left:none}

/* gallery */
.gallery{height:331px}
.gallery .section-title{color:var(--slate);padding-top:28px}
.gallery .section-title::after{background:var(--slate)}
.gallery-row{position:absolute;left:206px;top:113px;display:flex;gap:30px}
.pair{position:relative;width:242px;height:180px}
.shot{position:absolute;width:122px;height:165px;background:#fff;box-shadow:0 2px 6px rgba(0,0,0,.18);padding:5px;text-align:center;font-size:11px;color:var(--ink)}
.shot .ph{height:130px;margin-bottom:5px}
.shot.before{left:0;top:0}
.shot.after{left:118px;top:12px}
.ph.teeth{background:linear-gradient(180deg,#b7545a,#e9e1d8 50%,#a8444b)}
.gallery .arrow-left{position:absolute;left:158px;top:180px}
.gallery .arrow-right{position:absolute;left:1018px;top:180px}

/* blog */
.blog{height:383px;background:var(--soft)}
.blog .section-title{color:var(--slate);padding-top:38px}
.blog .section-title::after{background:var(--slate)}
.posts{position:absolute;left:155px;top:112px;display:flex;gap:36px;list-style:none}
.post{width:268px}
.post .num{font-family:"Oswald",Arial,sans-serif;font-size:32px;color:var(--slate);line-height:1;border-bottom:2px solid var(--slate);padding-bottom:4px;width:100%}
.post .date{font-size:10.5px;font-weight:600;color:var(--ink);margin-top:12px;letter-spacing:.3px}
.post h3{font-size:13.5px;font-weight:400;color:var(--ink);margin-top:12px;line-height:1.35;height:40px}
.post p{font-size:12px;color:var(--muted);margin-top:18px;line-height:1.5}
.post .more{display:inline-block;font-size:10.5px;font-weight:700;margin-top:18px;color:var(--ink);letter-spacing:.4px}
.blog .arrow-left{position:absolute;left:88px;top:212px}
.blog .arrow-right{position:absolute;left:1082px;top:212px}

/* testimonial */
.testimonial{height:340px;text-align:center}
.quote-mark{font-family:Georgia,serif;font-size:50px;color:var(--slate);padding-top:18px;line-height:1}
.quote-text{font-size:17px;color:var(--ink);line-height:1.55;margin-top:42px}
.quote-name{font-size:13px;font-weight:700;margin-top:40px;color:var(--ink)}
.quote-place{font-size:12px;color:var(--muted)}
.t-nav{position:absolute;top:172px;font-size:11px;font-weight:600;letter-spacing:2px;color:var(--muted)}
.t-prev{left:155px}
.t-next{left:990px}

/* footer */
.site-footer{height:436px;background:linear-gradient(var(--paper) 0 36px,var(--slate) 36px)}
.contact-strip{position:absolute;left:158px;top:0;width:884px;height:72px;display:flex}
.contact-strip div{flex:1;display:flex;align-items:center;gap:14px;padding-left:20px;color:#fff;font-size:12.5px;line-height:1.45}
.c-blue{background:var(--blue)}
.c-slate{background:var(--slate-dark)}
.contact-strip svg{width:26px;height:26px;flex:none}
.newsletter{position:absolute;left:0;top:104px;width:1200px;text-align:center;color:#fff}
.newsletter h2{font-size:21px;font-weight:600}
.newsletter h2::after{content:"";display:block;width:40px;height:2px;background:#fff;margin:6px auto 0}
.newsletter p{font-size:13.5px;margin-top:16px;line-height:1.5}
.subscribe{display:flex;justify-content:center;margin-top:20px}
.subscribe span{width:340px;height:32px;background:var(--blue);opacity:.55;display:block}
.subscribe b{width:95px;height:32px;background:var(--blue);display:flex;align-items:center;justify-content:center;gap:8px;font-size:13px}
.footer-socials{display:flex;justify-content:center;margin-top:24px;color:#fff}
.footer-socials .socials{color:#fff}
.footer-socials .socials i{background:#fff}
.footer-links{font-size:12px;margin-top:10px;line-height:1.9}
.footer-links span{margin:0 6px}
.copyright{position:absolute;left:0;bottom:0;width:1200px;height:36px;background:var(--slate-dark);color:#dbe2e6;font-size:11px;display:flex;align-items:center;justify-content:center}
</style>
</head>
<body>

<header class="site-header">
  <div class="wrap">
    <div class="brand"><span class="brand-dot"></span><span class="brand-name">Harborview Smile Glow</span></div>
    <div class="top-contact">
      <span class="call">Call Us &#9742; 555-204-7730</span>
      <span class="socials"><i></i><b>/</b><i></i><b>/</b><i></i><b>/</b><i></i><b>/</b><i></i><b>/</b><i></i></span>
    </div>
    <div class="top-buttons">
      <a class="btn btn-book">Book Appointment</a>
      <a class="btn btn-deal">Get Our $99 Teeth Whitening Deal</a>
    </div>
  </div>
</header>

<nav class="main-nav">
  <div class="wrap">
    <ul>
      <li class="active">Home</li><li>Our Process</li><li>Photos</li><li>White Smile Club</li><li>Testimonials</li><li>Appointments</li><li>FAQ</li><li>Contact</li><li>Blog</li><li>Buy Now</li>
    </ul>
  </div>
</nav>

<section class="hero">
  <div class="hero-photo" role="img" aria-label="Photo of smiling customers holding round signs in the clinic"></div>
  <svg class="hero-panel" viewBox="0 0 560 434" aria-hidden="true">
    <polygon points="0,0 380,0 533,352 492,434 0,434" fill="#44596a"/>
    <polyline points="392,0 545,352 504,434" fill="none" stroke="#1ba8d6" stroke-width="3"/>
  </svg>
  <div class="hero-text">
    <div class="kicker">Limited Time</div>
    <div class="special">Special $99</div>
    <div class="offer">Professional Laser Teeth Whitening</div>
    <a class="btn">Call Us &#9742; 555-204-7730</a>
  </div>
  <div class="hero-dots">
    <span class="circle-btn light"><svg width="10" height="10" viewBox="0 0 10 10"><path d="M7 1 3 5l4 4" fill="none" stroke="#44596a" stroke-width="2"/></svg></span>
    <span class="circle-btn blue"><svg width="10" height="10" viewBox="0 0 10 10"><path d="M3 1l4 4-4 4" fill="none" stroke="#fff" stroke-width="2"/></svg></span>
  </div>
</section>

<section class="welcome">
  <div class="welcome-text">
    <h1>Welcome to <span>Harborview Smile Glow</span></h1>
    <div class="lead">The best price, service and results</div>
    <p>Harborview Smile Glow features state-of-the-art technologies that are safe, industry-unique and very cost-effective. Our teeth whitening system utilizes the latest blue light whitening technology. Our Blue Light Systems are calibrated precisely for optimal activation of our exclusive hydrogen peroxide based whitening solution which is manufactured in a FDA registered facility in the USA.</p>
    <p>Our special lighting systems intensify the release of hydroxyl radicals that accelerate the dissipation of tooth stains. The entire teeth whitening process is accelerated and able to be completed in just 45 minutes with instant results.</p>
  </div>
  <div class="welcome-photo" role="img" aria-label="Photo of clinic staff with a happy customer holding a sign"></div>
</section>

<section class="why">
  <h2 class="section-title">Why Choose Us?</h2>
  <ul class="why-list">
    <li><svg viewBox="0 0 54 54" fill="none" stroke="#fff" stroke-width="2.4"><ellipse cx="18" cy="14" rx="12" ry="4"/><path d="M6 14v22c0 2 5 4 12 4M30 14v8"/><path d="M6 21c0 2 5 4 12 4M6 28c0 2 5 4 12 4"/><circle cx="35" cy="36" r="12"/><path d="M38 31h-5a2 2 0 0 0 0 4h4a2 2 0 0 1 0 4h-5M35 29v14"/></svg>Price</li>
    <li><svg viewBox="0 0 54 54" fill="none" stroke="#fff" stroke-width="2.4"><rect x="11" y="8" width="32" height="40" rx="3"/><rect x="20" y="5" width="14" height="6" rx="2"/><path d="M17 32l7-8 6 6 8-10"/><path d="M17 41h20"/></svg>Results</li>
    <li><svg viewBox="0 0 54 54" fill="none" stroke="#fff" stroke-width="2.4"><path d="M16 40c-3-5-4-10-4-14a15 15 0 0 1 30 0c0 6-2 11-5 16"/><path d="M20 42c-2-5-3-10-3-16a10 10 0 0 1 20 0c0 5-1 10-3 14"/><path d="M27 44c-2-6-3-12-3-18a3 3 0 0 1 6 0c0 6-1 11-2 15"/></svg>No Pain</li>
    <li><svg viewBox="0 0 54 54" fill="none" stroke="#fff" stroke-width="2.4"><circle cx="27" cy="27" r="7"/><path d="M27 6v7M27 41v7M6 27h7M41 27h7M12 12l5 5M37 37l5 5M42 12l-5 5M17 37l-5 5"/><circle cx="27" cy="27" r="15"/></svg>Service</li>
    <li><svg viewBox="0 0 54 54" fill="none" stroke="#fff" stroke-width="2.4"><path d="M44 27a17 17 0 1 1-5-12"/><path d="M40 8v8h-8"/><path d="M27 17v11l7 5"/></svg>Convenience</li>
  </ul>
</section>

<section class="how">
  <div class="how-photo" role="img" aria-label="Photo of two smiling customers holding a round clinic sign"></div>
  <div class="how-text">
    <h2>How It Works?</h2>
    <p>We have a very effective teeth whitening treatment that is guaranteed to get you quick results in about 1 hour. To start the treatment you'll apply a Hydrogen Peroxide based whitening agent to your teeth. We then place our cold blue light directly in front of your exposed teeth for 15 minutes per treatment. The lighting systems we use activate the whitening agent and thats what accelerates the whitening process, giving you whiter teeth in less than an hour.</p>
    <p>We always perform what we call a "Triple Treatment". So that's 3 of the 15 minute treatments all done consecutively, in the same visit. The actual whitening time is a total of 45 minutes. Now there is a few minute break in between each 15 minute treatment and this is why we tell all of our patients to give yourself one hour at the office.</p>
  </div>
</section>

<section class="compare">
  <h2 class="section-title">Compare Us</h2>
  <table class="compare-table">
    <thead>
      <tr><th>Price</th><th class="hl">LumaPro</th><th class="us">Harborview</th><th class="hl">GleamLab</th><th>Home Kits</th></tr>
    </thead>
    <tbody>
      <tr><td>Speed</td><td>1-2 Hours</td><td>45 Mins</td><td>7-14 Days</td><td>7-30 Days</td></tr>
      <tr><td>Ease Of Use</td><td>Difficult/Dentist</td><td>Very Easy</td><td>Difficult</td><td>Difficult</td></tr>
      <tr><td>Cost</td><td>$300-$600</td><td>$378</td><td>$300-$600</td><td>$50-$150</td></tr>
      <tr><td>Availability</td><td>Limited Availability</td><td>Appt Only</td><td>Limited Availability</td><td>Store Purchase</td></tr>
      <tr><td>Pain</td><td>Pain &amp; Sensitivity</td><td>No Pain</td><td>Sensitivity</td><td>Sensitivity</td></tr>
    </tbody>
  </table>
</section>

<section class="gallery">
  <h2 class="section-title">Photo Gallery</h2>
  <span class="circle-btn light arrow-left" style="border:1px solid #9aa6af"><svg width="10" height="10" viewBox="0 0 10 10"><path d="M7 1 3 5l4 4" fill="none" stroke="#44596a" stroke-width="2"/></svg></span>
  <div class="gallery-row">
    <div class="pair">
      <div class="shot before"><div class="ph teeth" role="img" aria-label="Close-up of teeth before whitening"></div>Before</div>
      <div class="shot after"><div class="ph teeth" role="img" aria-label="Close-up of teeth after whitening"></div>After</div>
    </div>
    <div class="pair">
      <div class="shot before"><div class="ph teeth" role="img" aria-label="Close-up of teeth before whitening"></div>Before</div>
      <div class="shot after"><div class="ph" style="background:linear-gradient(180deg,#6b7782,#a5adb4 50%,#5f6b75)" role="img" aria-label="Close-up of teeth after whitening"></div>After</div>
    </div>
    <div class="pair">
      <div class="shot before"><div class="ph teeth" role="img" aria-label="Close-up of teeth before whitening"></div>Before</div>
      <div class="shot after"><div class="ph teeth" role="img" aria-label="Close-up of teeth after whitening"></div>After</div>
    </div>
  </div>
  <span class="circle-btn slate arrow-right"><svg width="10" height="10" viewBox="0 0 10 10"><path d="M3 1l4 4-4 4" fill="none" stroke="#fff" stroke-width="2"/></svg></span>
</section>

<section class="blog">
  <h2 class="section-title">Our Latest Blog</h2>
  <span class="circle-btn slate arrow-left"><svg width="10" height="10" viewBox="0 0 10 10"><path d="M7 1 3 5l4 4" fill="none" stroke="#fff" stroke-width="2"/></svg></span>
  <ul class="posts">
    <li class="post"><div class="num">01</div><div class="date">OCTOBER 27, 2016</div><h3>Teeth Whitening – All Natural Alternative</h3><p>In today's society, a healthy white smile is important not only because of its obvious health benefits. It also increases…</p><span class="more">READ MORE</span></li>
    <li class="post"><div class="num">02</div><div class="date">MAY 9, 2016</div><h3>Harborview Smile Glow Whitening Center</h3><p>At Harborview Smile Glow we offer an affordable and effective teeth whitening service that is bound to have…</p><span class="more">READ MORE</span></li>
    <li class="post"><div class="num">03</div><div class="date">APRIL 27, 2016</div><h3>Teeth Whitening In Harborview</h3><p>Were you aware that teeth whitening is the most common procedure practiced in dentistry? It's true, and while this…</p><span class="more">READ MORE</span></li>
  </ul>
  <span class="circle-btn slate arrow-right"><svg width="10" height="10" viewBox="0 0 10 10"><path d="M3 1l4 4-4 4" fill="none" stroke="#fff" stroke-width="2"/></svg></span>
</section>

<section class="testimonial">
  <div class="quote-mark">&ldquo;</div>
  <p class="quote-text">Wow... What a terrific experience!<br>Professional, state-of-the-art equipment and the whole team was wonderful!<br>I will definitely be returning when I'm back in Harborview!<br>I highly recommend this service, exceptional!</p>
  <div class="quote-name">DANA L.</div>
  <div class="quote-place">Mill Creek, OR</div>
  <span class="t-nav t-prev">&larr; PREV</span>
  <span class="t-nav t-next">NEXT &rarr;</span>
</section>

<footer class="site-footer">
  <div class="contact-strip">
    <div class="c-blue"><svg viewBox="0 0 26 26" fill="none" stroke="#fff" stroke-width="2"><path d="M13 24s-8-8-8-14a8 8 0 0 1 16 0c0 6-8 14-8 14z"/><circle cx="13" cy="10" r="3"/></svg><span>418 Harbor Crest Way Ste 12<br>Harborview, CA 90000</span></div>
    <div class="c-slate"><svg viewBox="0 0 26 26" fill="none" stroke="#fff" stroke-width="2"><path d="M6 3h5l2 6-3 2a14 14 0 0 0 5 5l2-3 6 2v5a2 2 0 0 1-2 2A19 19 0 0 1 4 5a2 2 0 0 1 2-2z"/></svg><span>Phone:<br>555-318-4402 &nbsp;|&nbsp; 800-555-0147</span></div>
    <div class="c-blue"><svg viewBox="0 0 26 26" fill="none" stroke="#fff" stroke-width="2"><rect x="3" y="6" width="20" height="14" rx="1"/><path d="M3 7l10 7 10-7"/></svg><span>Email:<br>hello@harborviewsmileglow.com</span></div>
  </div>
  <div class="newsletter">
    <h2>Newsletter</h2>
    <p>You Want to get Update about anything News?<br>Join our newsletter</p>
    <div class="subscribe"><span></span><b>&#10148; Send</b></div>
    <div class="footer-socials"><span class="socials"><i></i><b>/</b><i></i><b>/</b><i></i><b>/</b><i></i><b>/</b><i></i><b>/</b><i></i></span></div>
    <div class="footer-links">
      Home<span>|</span>Our Process<span>|</span>Photos<span>|</span>White Smile Club<span>|</span>Testimonials<span>|</span>Contact<span>|</span>After Care<span>|</span>Consent Form English<span>|</span>Consent Form Espanol<br>
      Consent Form English<span>|</span>Cancellation Policy<span>|</span>Privacy Policy
    </div>
  </div>
  <div class="copyright">© 2017 Harborview Smile Glow</div>
</footer>

</body>
</html>
```